Tessaro Lane Website

We are starting a marketing company and to do that we need a website! We want a website that will inspire and persuade to bring out the awesomeness in our clients.
What we want to see:
- Inspirational and persuasive imagery that relate to Branding.
- No cliche images eg. business man, suits and hand shakes
- We want to transform and educate our clients.
- We want to show them the path and would like our website to really act as a guide that guides them step by step through our process.
- We want the portray that we are an investment but not have a pretentious way to it. We put our heart into every project and that is how we treat our clients.
-When you submit your design please include what platform you have created for. Preference would be Wordpress or Joobla.

We have included the psd file for the wire frame, logo files, font files, site map and a link to a video we create to give you more information on what we would like to see. http://clipvault-demo.example/t/qx903LmaP

Feel free to make small modification to the logos if you think it will improve it. Your creativity and advice is most welcome.

One thing we forgot. We would like to have our contact information near the top of the website as well as at the bottom.  Here is out contact info:

Email: info@tessarolane.ca
Phone: 555-013-4829

Reason: As we are new with the platform and that we want to optimize our results, we decided to extend the deadline by 15 days. Thanks!

Target Market(s)

28-60, Male and Female, Oil field, Local Businesses, Dentists, Chiropractors, Hair salon, Construction/Renovation, Events etc

Industry/Entity Type

Investment

Requirements
Must have
• - 4 Inspirational and persuasive Imagery for the top portion of the website
- Must have a feel as if your not on a website an example of this is linked below.
http://www.pitchgallery-demo.example/design/482907/web-design-by-dalia-fenwick
Nice to have
• - Creative advice from you.
- Creative buttons for Get Free Quote and Subscribe buttons. Something out of the box that draws peoples attention. eg. a 'B' button. Just and example but still something related to branding.
Should not have
• No Cliches

```html
<!DOCTYPE html>
<html lang="en">
<head>
<meta charset="utf-8">
<title>Tessaro Lane</title>
<link rel="stylesheet" href="https://fonts.googleapis.com/css2?family=Arimo:wght@400;700&display=swap">
<style>
  :root {
    --ink: #2d3040;
    --nav-active: #474c66;
    --nav-text: #8a8d9c;
    --body-text: #7a7a7a;
    --link: #1f7fd6;
    --panel: #f2f2f2;
    --green-top: #9cc45a;
    --green-bottom: #6c9a2c;
    --tab-dark: rgba(58, 60, 34, 0.62);
    --tab-line: rgba(255, 255, 255, 0.25);
    --white: #ffffff;
    --footer-muted: #6b6e80;
  }
  * { box-sizing: border-box; margin: 0; padding: 0; }
  html, body { width: 1200px; height: 823px; overflow: hidden; }
  body { position: relative; background: var(--white); font-family: "Arimo", Arial, sans-serif; }

  .top-bar { position: absolute; left: 0; top: 0; width: 1200px; height: 41px; background: var(--ink); }
  .brand-card {
    position: absolute; left: 118px; top: 0; width: 189px; height: 76px; background: var(--white);
    box-shadow: 0 2px 6px rgba(0,0,0,0.35); z-index: 3;
    display: flex; align-items: center; gap: 10px; padding-left: 20px;
  }
  .brand-mark { width: 18px; height: 18px; background: var(--green-bottom); }
  .brand-name { font-size: 21px; font-weight: 700; color: var(--green-bottom); line-height: 1; }

  .site-nav a {
    position: absolute; top: 0; height: 41px; line-height: 42px; text-align: center;
    font-size: 16px; font-weight: 700; color: var(--nav-text); text-decoration: none;
  }
  .site-nav .is-active { background: var(--nav-active); color: var(--white); }
  .nav-pointer { position: absolute; left: 845px; top: 41px; width: 0; height: 0;
    border-left: 7px solid transparent; border-right: 7px solid transparent; border-top: 7px solid var(--nav-active); z-index: 2; }

  .social-links { position: absolute; left: 955px; top: 9px; display: flex; gap: 6px; }
  .social-links span { width: 24px; height: 24px; border-radius: 4px; display: block; }
  .social-links .s1 { background: #3b5a98; }
  .social-links .s2 { background: #3aa6dc; }
  .social-links .s3 { background: #d22a22; }
  .social-links .s4 { background: #d9402f; }

  .hero {
    position: absolute; left: 0; top: 41px; width: 1200px; height: 294px;
    background: linear-gradient(180deg, #b9d3e6 0%, #a7c28a 28%, #86a84a 60%, #6f8c36 100%);
  }

  .section-tabs { position: absolute; left: 117px; top: 274px; height: 61px; display: flex; z-index: 2; }
  .section-tabs a {
    width: 160px; height: 61px; display: flex; align-items: center; justify-content: center;
    font-size: 21px; font-weight: 700; color: var(--white); text-decoration: none;
    background: var(--tab-dark); border-left: 1px solid var(--tab-line);
  }
  .section-tabs .is-current { background: var(--white); color: var(--ink); border-left: none; }
  .section-tabs .quote-button {
    margin-left: 2px; width: 159px; flex-direction: column; font-size: 18px; line-height: 18px;
    background: linear-gradient(180deg, var(--green-top), var(--green-bottom)); border: 1px solid #5f8a25;
  }

  .main-content { position: absolute; left: 158px; top: 367px; width: 575px; }
  .main-content h1 { font-size: 22px; color: var(--ink); margin-bottom: 16px; }
  .main-content p { font-size: 15.5px; line-height: 22px; color: var(--body-text); margin-bottom: 22px; }
  .main-content a { color: var(--link); }

  .newsletter {
    position: absolute; left: 760px; top: 408px; width: 285px; height: 166px;
    background: var(--panel); border-radius: 6px; padding: 26px 0 0 50px;
  }
  .newsletter h2 { font-size: 20px; color: #3a3a3a; }
  .newsletter p { font-size: 14px; color: var(--body-text); margin-top: 6px; }
  .subscribe-button {
    display: block; margin-top: 17px; width: 191px; height: 46px; line-height: 46px; text-align: center;
    font-size: 20px; font-weight: 700; color: var(--white); text-decoration: none;
    background: linear-gradient(180deg, var(--green-top), var(--green-bottom)); border: 1px solid #5f8a25;
  }

  .site-footer { position: absolute; left: 0; top: 727px; width: 1200px; height: 96px; background: var(--ink); }
  .footer-links { position: absolute; left: 117px; top: 15px; display: flex; gap: 13px; }
  .footer-links a { font-size: 15px; color: var(--white); text-decoration: none; }
  .copyright { position: absolute; right: 139px; top: 17px; font-size: 13px; color: var(--footer-muted); }
</style>
</head>
<body>
  <header class="top-bar">
    <nav class="site-nav">
      <a href="#" style="left:340px;width:140px;">Tessaro Lane</a>
      <a href="#" style="left:500px;width:126px;">Be Found</a>
      <a href="#" style="left:640px;width:126px;">Connect</a>
      <a href="#" class="is-active" style="left:781px;width:143px;">Get Growing</a>
    </nav>
    <div class="social-links"><span class="s1"></span><span class="s2"></span><span class="s3"></span><span class="s4"></span></div>
  </header>
  <div class="nav-pointer"></div>
  <a class="brand-card" href="#"><span class="brand-mark"></span><span class="brand-name">Tessaro Lane</span></a>

  <div class="hero" role="img" aria-label="Close-up of a green wheat field under a pale blue sky"></div>

  <nav class="section-tabs">
    <a href="#" class="is-current">Strategy</a>
    <a href="#">Portfolio</a>
    <a href="#">About Us</a>
    <a href="#">Contact Us</a>
    <a href="#">Blog</a>
    <a href="#" class="quote-button"><span>Get a</span><span>Free Quote</span></a>
  </nav>

  <main class="main-content">
    <h1>Main Headline</h1>
    <p>Morbi ac commodo nulla. In condimentum orci id nisl volutpat bibendum. Quisque commodo hendrerit lorem quis egestas. Maecenas quis tortor arcu. Vivamus rutrum nunc non neque consectetur quis placerat neque lobortis.</p>
    <p>Nam vestibulum, arcu sodales feugiat consectetur, nisl orci bibendum elit, eu euismod magna sapien ut nibh. Donec <a href="#">sample link</a> tortor dictum gravida. In hac habitasse platea dictumst. Nam pulvinar, odio sed rhoncus suscipit, sem diam ultrices mauris, eu consequat purus metus eu velit. Proin metus odio, aliquam eget molestie nec, gravida ut sapien.</p>
    <p>Phasellus quis est sed turpis sollicitudin venenatis sed eu odio. Praesent eget neque.</p>
  </main>

  <aside class="newsletter">
    <h2>Get Tips and Tricks!</h2>
    <p>Subscribe to our Newsletter.</p>
    <a href="#" class="subscribe-button">Subscribe</a>
  </aside>

  <footer class="site-footer">
    <nav class="footer-links">
      <a href="#">Site Map</a><a href="#">Strategy</a><a href="#">Portfolio</a><a href="#">About Us</a><a href="#">Contact Us</a><a href="#">Blog</a>
    </nav>
    <div class="copyright">©TESSARO LANE INC. 2013</div>
  </footer>
</body>
</html>
```